Business Card Design

Its a residential construction company

Industry/Entity Type

Residential

Contact Information for Business Card

Velbrook Homes Pty Ltd,
Dane T Halloway
BE (Civil), Grad.Dip Hwy, Eng. (QPTU), FRC.Aust,
Director, Velbrook Homes Pty Ltd

PO Box 487, Harlow Vale, NSW, 2790. Tel: 048726 5531
email: dane@velbrookhomes.com

```html
<!DOCTYPE html>
<html lang="en">
<head>
<meta charset="utf-8">
<title>Velbrook Homes Pty Ltd – Business Card</title>
<link rel="stylesheet" href="https://fonts.googleapis.com/css2?family=Montserrat:wght@800&family=Didact+Gothic&family=Roboto+Condensed:ital,wght@1,700&display=swap">
<style>
  :root {
    --ink: #111111;
    --card-white: #ffffff;
    --sky-pale: #eef5fc;
    --sky-light: #a9d2ee;
    --sky-deep: #0094d6;
  }
  * { margin: 0; padding: 0; box-sizing: border-box; }
  html, body {
    width: 1200px;
    height: 742px;
    overflow: hidden;
    background: var(--card-white);
  }
  .card {
    position: relative;
    width: 1200px;
    height: 742px;
    overflow: hidden;
    color: var(--ink);
    background: linear-gradient(90deg,
      var(--card-white) 0%,
      var(--card-white) 30%,
      var(--sky-pale) 50%,
      var(--sky-light) 80%,
      var(--sky-deep) 100%);
  }
  .brand {
    position: absolute;
    left: 96px;
    top: 244px;
    display: flex;
    align-items: center;
    gap: 18px;
    font-family: "Montserrat", sans-serif;
    font-weight: 800;
    font-size: 44px;
    line-height: 1;
    color: var(--ink);
    text-transform: uppercase;
    white-space: nowrap;
  }
  .brand-square {
    width: 28px;
    height: 28px;
    background: var(--ink);
  }
  .monogram {
    position: absolute;
    left: 972px;
    top: 205px;
    width: 160px;
    font-family: "Montserrat", sans-serif;
    font-weight: 800;
    font-size: 28px;
    line-height: 1.3;
    text-align: center;
    text-transform: uppercase;
    color: var(--ink);
  }
  .phone {
    position: absolute;
    left: 96px;
    top: 352px;
    font-family: "Montserrat", sans-serif;
    font-weight: 800;
    font-size: 44px;
    line-height: 1.2;
    letter-spacing: 1px;
    color: var(--ink);
  }
  .credentials {
    position: absolute;
    left: 100px;
    top: 428px;
    font-family: "Didact Gothic", sans-serif;
    font-size: 29px;
    line-height: 44px;
    text-transform: uppercase;
    white-space: nowrap;
    color: var(--ink);
  }
  .email {
    position: absolute;
    left: 97px;
    top: 618px;
    font-family: "Roboto Condensed", sans-serif;
    font-style: italic;
    font-weight: 700;
    font-size: 35px;
    line-height: 1.1;
    text-transform: uppercase;
    color: var(--ink);
  }
</style>
</head>
<body>
  <main class="card">
    <div class="brand">
      <span class="brand-square"></span>
      <span class="brand-name">Velbrook Homes Pty Ltd</span>
    </div>

    <div class="monogram">Velbrook<br>Homes<br>Pty Ltd</div>

    <p class="phone">TEL: 048726 5531</p>

    <p class="credentials">
      Dane T Halloway BE (Civil),<br>
      Grad.Dip Hwy, Eng. (QPTU), FRC.Aust,<br>
      Director, Velbrook Homes Pty Ltd PO Box 487,<br>
      Harlow Vale, NSW, 2790.
    </p>

    <p class="email">Email: dane@velbrookhomes.com</p>
  </main>
</body>
</html>
```